Torvane Center for Restorative Medicine

I need a full informational website for my medical practice. I would like to use my logo and also include a lot of emblems/pictures (also a picture of me in a white coat). The website should have a function for people to inquire and send me messages. I will be offering needle-less regenerative injection therapy, stem cell treatments, bioidentical hormone therapy, treatment for chronic illness, neurodegenerative diseases, skin rejuvenation, hair restoration, male enhancement, female enhancement, and anti-aging. The practice will not be accepting insurance and will be cash/credit card only.
A good example of written content and functionality is this website:
http://thebqvx.example/. However, I want different theme and tones.
Target Market(s)
High end clientele in Los Angeles, Southern California. Health minded people who are interested in living better and longer and can afford anti-aging treatments. Men and women who want to improve sexual health and wellbeing.
Industry/Entity Type
Medical And Science
Coding
Coded - Design and coding required
Number of Pages Required
5+ page
Font styles to use
Requirements
Must have
- 1. I will need to be able to move the site to other servers (needed for site speed)
- 2. Site must be build on WordPress
- 3. Full admin credentials for domain, cpanel, wordpress, ftp.
- 4. No third party interaction on development and content deployment once the site is on different servers
- 5. I will need the ability to add content and links to the site
- 6. I will need the ability to optimize the site for speed
- 7. I will need to ability to modify URLs so they are more SEO friendly
Nice to have
- pictures of stem cells, health improvement and regeneration, beauty, youthful individuals, older healthy and happy individuals. Medical designs.
Should not have
- flowers, dna

```html
<!DOCTYPE html>
<html lang="en">
<head>
<meta charset="utf-8">
<title>Torvane Center for Restorative Medicine</title>
<link href="https://fonts.googleapis.com/css2?family=Cinzel:wght@400;700&family=Open+Sans:wght@400;600;700&display=swap" rel="stylesheet">
<style>
:root{
  --navy:#1c2a78;
  --navy-deep:#101d63;
  --green:#1fa06a;
  --badge-bg:#e8edf6;
  --text:#666b73;
  --ink:#222;
  --line:#e3e6ea;
  --svc-bg:#eef2f4;
  --white:#fff;
}
*{box-sizing:border-box;margin:0;padding:0}
html,body{width:1200px;height:3636px;overflow:hidden}
body{position:relative;font-family:"Open Sans",Arial,sans-serif;color:var(--text);background:var(--white)}
.abs{position:absolute}

/* header */
.site-header{position:absolute;left:0;top:0;width:1200px;height:121px;background:var(--white);border-top:4px solid var(--green)}
.brand{position:absolute;left:98px;top:38px;display:flex;align-items:center;gap:12px}
.brand-dot{width:34px;height:34px;border-radius:50%;background:var(--green)}
.brand-name{font-family:"Cinzel",Georgia,serif;font-weight:700;font-size:30px;color:var(--navy);letter-spacing:1px}
.topline{position:absolute;right:98px;top:30px;font-size:15px;color:var(--text);display:flex;gap:18px;align-items:center}
.topline svg{vertical-align:-3px;margin-right:6px}
.nav{position:absolute;right:98px;top:74px;display:flex;gap:36px;font-size:15px;font-weight:700;color:#222}

/* hero */
.hero{position:absolute;left:0;top:121px;width:1200px;height:606px;overflow:hidden}
.hero-photo{position:absolute;inset:0;background:linear-gradient(100deg,#5a4a3a 0%,#7e7a5f 35%,#a7a88a 55%,#c9b6a0 75%,#6f7d5c 100%)}
.hero-shade{position:absolute;inset:0;background:linear-gradient(90deg,rgba(0,0,0,.35),rgba(0,0,0,0) 60%)}
.hero-title{position:absolute;left:123px;top:186px;font-family:"Cinzel",Georgia,serif;font-weight:400;font-size:50px;color:#fff;letter-spacing:1px}
.hero-text{position:absolute;left:123px;top:262px;width:490px;font-size:21px;line-height:30px;color:#fff}
.btn-ghost{position:absolute;left:124px;top:352px;width:172px;height:44px;border:2px solid #fff;border-radius:22px;color:#fff;font-size:14px;font-weight:700;display:flex;align-items:center;justify-content:center;gap:6px}
.hero-arrow{position:absolute;top:270px;width:40px;height:40px;border-radius:50%;background:rgba(0,0,0,.55);display:flex;align-items:center;justify-content:center}
.dots{position:absolute;left:546px;top:528px;display:flex;gap:10px}
.dots span{width:17px;height:17px;border-radius:50%;border:2px solid #fff}
.dots span.on{background:#fff}

.badge{position:absolute;width:96px;height:96px;border-radius:50%;background:var(--badge-bg);color:var(--navy);font-weight:700;font-size:28px;display:flex;align-items:center;justify-content:center}

/* sections */
h2.section-title{position:absolute;width:1200px;left:0;text-align:center;font-family:"Cinzel",Georgia,serif;font-weight:400;font-size:32px;color:#1a1a1a;letter-spacing:1px}
.lead{position:absolute;width:1200px;left:0;text-align:center;font-size:13px;line-height:26px;color:var(--text)}
.about-title{position:absolute;left:97px;top:978px;font-family:"Cinzel",Georgia,serif;font-size:23px;color:var(--navy)}
.about-text{position:absolute;left:97px;top:1040px;width:545px;font-size:13.5px;line-height:24px}
.about-text p+p{margin-top:20px}
.btn{position:absolute;height:42px;border-radius:21px;background:var(--green);color:#fff;font-size:14px;font-weight:700;display:flex;align-items:center;justify-content:center;gap:6px}
.video-frame{position:absolute;left:732px;top:977px;width:412px;height:264px;border:2px solid var(--navy)}
.video{position:absolute;left:688px;top:1018px;width:412px;height:267px;border:6px solid #fff;box-shadow:0 2px 10px rgba(0,0,0,.2);background:linear-gradient(120deg,#dfe6ea,#f3f2ef 40%,#c9d6dd 70%,#9fb3bf)}
.play{position:absolute;left:176px;top:108px;width:52px;height:38px;border-radius:10px;background:#d62a2a;display:flex;align-items:center;justify-content:center}

.services{position:absolute;left:0;top:1394px;width:1200px;height:788px;background:var(--svc-bg)}
.svc-card{position:absolute;top:1612px;width:223px;height:376px;background:#fff;box-shadow:0 2px 8px rgba(0,0,0,.12);text-align:center}
.svc-img{position:absolute;left:0;top:0;width:223px;height:150px;clip-path:polygon(0 0,100% 0,100% 75%,50% 100%,0 75%)}
.svc-icon{position:absolute;left:79px;top:132px;width:64px;height:64px;border-radius:50%;background:var(--green);border:4px solid #fff;display:flex;align-items:center;justify-content:center}
.svc-name{position:absolute;left:10px;top:218px;width:203px;font-size:14.5px;font-weight:700;color:#222;line-height:22px}
.svc-text{position:absolute;left:14px;top:268px;width:195px;font-size:12px;line-height:20px;color:var(--text)}
.pill{position:absolute;left:52px;top:358px;width:118px;height:34px;border-radius:17px;background:#fff;border:1px solid #ccd;box-shadow:0 1px 4px rgba(0,0,0,.15);font-size:12.5px;font-weight:700;color:#222;display:flex;align-items:center;justify-content:center;gap:5px}

.news-card{position:absolute;top:2351px;width:484px;height:218px;background:#fff;box-shadow:0 1px 6px rgba(0,0,0,.12)}
.news-img{position:absolute;left:0;top:0;width:192px;height:218px}
.news-body{position:absolute;left:218px;top:24px;width:245px}
.news-title{font-size:17px;font-weight:700;color:#222;letter-spacing:.3px}
.news-date{margin-top:8px;font-size:12.5px;color:var(--navy);font-weight:600}
.news-text{margin-top:12px;font-size:12.5px;line-height:20px}
.news-foot{margin-top:16px;display:flex;justify-content:space-between;font-size:12.5px}
.news-foot b{color:var(--green)}

.rule{position:absolute;left:99px;top:2662px;width:1004px;height:2px;background:var(--line)}

.quote-card{position:absolute;top:2860px;width:306px;height:206px;background:#fff;box-shadow:0 1px 6px rgba(0,0,0,.13);text-align:center}
.avatar{position:absolute;left:110px;top:-42px;width:86px;height:86px;border-radius:50%;border:4px solid #fff;box-shadow:0 1px 6px rgba(0,0,0,.2)}
.quote-mark{position:absolute;left:140px;top:30px;width:26px;height:26px;border-radius:50%;background:var(--green);color:#fff;font-size:18px;line-height:30px;font-weight:700}
.stars{position:absolute;left:0;top:62px;width:306px;color:#f2b20c;font-size:17px;letter-spacing:2px}
.quote{position:absolute;left:26px;top:90px;width:254px;font-size:12px;line-height:19px;font-style:italic}
.who{position:absolute;left:0;top:172px;width:306px;font-size:12.5px;color:#222}
.side-arrow{position:absolute;top:2917px;width:46px;height:46px;border-radius:50%;background:#fff;box-shadow:0 1px 6px rgba(0,0,0,.2);display:flex;align-items:center;justify-content:center}

/* footer */
.footer-curve{position:absolute;left:0;top:3180px;width:1200px;height:100px}
.footer{position:absolute;left:0;top:3252px;width:1200px;height:384px;background:var(--navy-deep);color:#fff}
.f-head{position:absolute;top:24px;font-size:16px;font-weight:700;text-decoration:underline;text-underline-offset:5px;letter-spacing:.3px}
.f-links{position:absolute;left:99px;top:66px;list-style:none;font-size:14px}
.f-links li{height:30px;display:flex;gap:18px;align-items:center}
.f-links li:before{content:"»";font-size:16px}
.f-contact{position:absolute;left:296px;top:68px;width:340px;font-size:14px;line-height:22px}
.f-row{display:flex;gap:22px;align-items:center;margin-bottom:24px}
.f-row svg{flex:none}
.f-note{position:absolute;left:671px;top:70px;width:440px;font-size:14px;line-height:26px}
.field{position:absolute;height:41px;border:1px solid #fff;font-size:13px;padding:12px 14px;color:#fff}
.submit{position:absolute;left:892px;top:188px;width:208px;height:41px;background:var(--green);font-weight:700;font-size:17px;display:flex;align-items:center;justify-content:center}
.f-rule{position:absolute;left:99px;top:292px;width:1004px;height:1px;background:rgba(255,255,255,.25)}
.copy{position:absolute;left:99px;top:330px;font-size:13.5px}
.follow{position:absolute;left:831px;top:325px;font-size:21px;font-weight:600;letter-spacing:.5px}
.socials{position:absolute;left:966px;top:322px;display:flex;gap:8px}
.socials span{width:30px;height:30px;border-radius:50%;border:2px solid #fff}
</style>
</head>
<body>

<header class="site-header">
  <div class="brand"><span class="brand-dot"></span><span class="brand-name">TORVANE</span></div>
  <div class="topline">
    <span><svg width="16" height="16" viewBox="0 0 24 24"><path fill="#1fa06a" d="M6.6 10.8a15 15 0 0 0 6.6 6.6l2.2-2.2c.3-.3.7-.4 1-.2 1.1.4 2.3.6 3.6.6.6 0 1 .4 1 1V20c0 .6-.4 1-1 1A17 17 0 0 1 3 4c0-.6.4-1 1-1h3.5c.6 0 1 .4 1 1 0 1.3.2 2.5.6 3.6.1.3 0 .7-.2 1z"/></svg>(+1) 123 456 7890</span>
    <span>|</span>
    <span><svg width="16" height="16" viewBox="0 0 24 24"><path fill="#1fa06a" d="M2 5h20v14H2zM4 7v.5l8 5 8-5V7z"/></svg>torvanerestorative.example</span>
  </div>
  <nav class="nav"><span>HOME</span><span>ABOUT US</span><span>SERVICES</span><span>TESTIMONIALS</span><span>BLOG</span><span>CONTACT</span></nav>
</header>

<section class="hero">
  <div class="hero-photo" role="img" aria-label="Photo of a woman in sportswear drinking from a water bottle outdoors"></div>
  <div class="hero-shade"></div>
  <h1 class="hero-title">TORVANE CENTER</h1>
  <p class="hero-text">Lorem ipsum dolor sit amet, consectetur adipiscing elit sed do eiusmod tempor incididunt.</p>
  <div class="btn-ghost">READ MORE <svg width="14" height="14" viewBox="0 0 14 14"><circle cx="7" cy="7" r="7" fill="#fff"/><path d="M5.5 4l3 3-3 3" stroke="#555" stroke-width="1.6" fill="none"/></svg></div>
  <div class="hero-arrow" style="left:38px"><svg width="14" height="14" viewBox="0 0 14 14"><path d="M9 2L4 7l5 5" stroke="#fff" stroke-width="2.2" fill="none"/></svg></div>
  <div class="hero-arrow" style="left:1120px"><svg width="14" height="14" viewBox="0 0 14 14"><path d="M5 2l5 5-5 5" stroke="#fff" stroke-width="2.2" fill="none"/></svg></div>
  <div class="dots"><span></span><span class="on"></span><span></span><span></span></div>
  <svg class="abs" style="left:0;top:470px" width="1200" height="140" viewBox="0 0 1200 140">
    <path d="M0 40 Q600 230 1200 40 L1200 140 L0 140Z" fill="#fff"/>
    <path d="M0 40 Q600 230 1200 40" stroke="#1fa06a" stroke-width="6" fill="none"/>
  </svg>
</section>

<div class="badge" style="left:48px;top:792px">01</div>
<h2 class="section-title" style="top:820px;font-size:30px">WELCOME TO TORVANE CENTER</h2>
<p class="lead" style="top:878px">Lorem ipsum dolor sit amet, consectetur adipiscing elit, sed do eiusmod tempor incididunt ut labore et dolore magna aliqua.<br>Ut enim ad minim veniam, quis nostrud exercitation ullamco laboris nisi ut aliquip ex ea commodo</p>

<h3 class="about-title">ABOUT OUR HEALTH THERAPY</h3>
<div class="about-text">
  <p>The following values drive how we operate our business and influence our CI's investment decision making. It is our belief that these play an important part in CI being able to sort opportunities into the genuine investment category and those that are not "bona fide". The CI values are critical in guiding our thinking through changing times.</p>
  <p>These attributes are also embedded in CI's performance reviews and staff are evaluated and rewarded on their adherence to these values.</p>
</div>
<div class="btn" style="left:99px;top:1246px;width:158px">READ MORE <svg width="14" height="14" viewBox="0 0 14 14"><circle cx="7" cy="7" r="7" fill="#fff"/><path d="M5.5 4l3 3-3 3" stroke="#1fa06a" stroke-width="1.6" fill="none"/></svg></div>
<div class="video-frame"></div>
<div class="video" role="img" aria-label="Video still of a doctor in a white coat at her desk">
  <div class="play"><svg width="18" height="18" viewBox="0 0 18 18"><path d="M5 3l10 6-10 6z" fill="#fff"/></svg></div>
</div>

<section class="services"></section>
<h2 class="section-title" style="top:1470px">OUR SERVICES</h2>
<p class="lead" style="top:1532px">At vero eos et accusamus et iusto odio dignissimos ducimus qui blanditiis praesentium.<br>voluptatum deleniti atque corrupti quos dolores</p>
<div class="badge" style="left:1046px;top:1460px">02</div>

<article class="svc-card" style="left:99px">
  <div class="svc-img" role="img" aria-label="Photo of an elderly man with a caregiver" style="background:linear-gradient(135deg,#7a6f66,#b7a79a 50%,#5d5650)"></div>
  <div class="svc-icon"><svg width="30" height="30" viewBox="0 0 30 30"><circle cx="15" cy="15" r="11" fill="none" stroke="#fff" stroke-width="2.4"/><path d="M15 5v20M8 11h14M8 19h14" stroke="#fff" stroke-width="2"/></svg></div>
  <div class="svc-name">NEURODEGENERATIVE DISEASES</div>
  <p class="svc-text">Nemo enim ipsam voluptatem quia voluptas sit aspertur aut odit aut conse magni dolores eos</p>
  <div class="pill">READ MORE <svg width="12" height="12" viewBox="0 0 14 14"><circle cx="7" cy="7" r="7" fill="#222"/><path d="M5.5 4l3 3-3 3" stroke="#fff" stroke-width="1.6" fill="none"/></svg></div>
</article>
<article class="svc-card" style="left:359px">
  <div class="svc-img" role="img" aria-label="Illustration of stem cells in a dark blue field" style="background:radial-gradient(circle at 40% 40%,#3f7fb0,#12304f 70%)"></div>
  <div class="svc-icon"><svg width="30" height="30" viewBox="0 0 30 30"><circle cx="10" cy="11" r="5" fill="none" stroke="#fff" stroke-width="2.2"/><circle cx="20" cy="19" r="5" fill="none" stroke="#fff" stroke-width="2.2"/><circle cx="21" cy="8" r="2.5" fill="#fff"/></svg></div>
  <div class="svc-name">STEM CELL TREATMENTS THERAPY</div>
  <p class="svc-text">Nemo enim ipsam voluptatem quia voluptas sit aspertur aut odit aut conse magni dolores eos</p>
  <div class="pill">READ MORE <svg width="12" height="12" viewBox="0 0 14 14"><circle cx="7" cy="7" r="7" fill="#222"/><path d="M5.5 4l3 3-3 3" stroke="#fff" stroke-width="1.6" fill="none"/></svg></div>
</article>
<article class="svc-card" style="left:618px">
  <div class="svc-img" role="img" aria-label="Photo of a doctor handing medication to a patient" style="background:linear-gradient(135deg,#c9c4b8,#e8d7c4 50%,#8aa4b5)"></div>
  <div class="svc-icon"><svg width="30" height="30" viewBox="0 0 30 30"><circle cx="13" cy="17" r="6" fill="none" stroke="#fff" stroke-width="2.2"/><path d="M17 13l7-7M19 6h5v5" stroke="#fff" stroke-width="2.2" fill="none"/></svg></div>
  <div class="svc-name">BIOIDENTICAL HORMONE THERAPY</div>
  <p class="svc-text">Nemo enim ipsam voluptatem quia voluptas sit aspertur aut odit aut conse magni dolores eos</p>
  <div class="pill">READ MORE <svg width="12" height="12" viewBox="0 0 14 14"><circle cx="7" cy="7" r="7" fill="#222"/><path d="M5.5 4l3 3-3 3" stroke="#fff" stroke-width="1.6" fill="none"/></svg></div>
</article>
<article class="svc-card" style="left:877px">
  <div class="svc-img" role="img" aria-label="Photo of a person holding an aching knee" style="background:linear-gradient(135deg,#c58f73,#e4bfa4 50%,#8e6a55)"></div>
  <div class="svc-icon"><svg width="30" height="30" viewBox="0 0 30 30"><path d="M15 4v22M6 10l9 5 9-5M9 26l6-6 6 6" stroke="#fff" stroke-width="2.2" fill="none"/></svg></div>
  <div class="svc-name">TREATMENT FOR CHRONIC ILLNESS</div>
  <p class="svc-text">Nemo enim ipsam voluptatem quia voluptas sit aspertur aut odit aut conse magni dolores eos</p>
  <div class="pill">READ MORE <svg width="12" height="12" viewBox="0 0 14 14"><circle cx="7" cy="7" r="7" fill="#222"/><path d="M5.5 4l3 3-3 3" stroke="#fff" stroke-width="1.6" fill="none"/></svg></div>
</article>
<div class="btn" style="left:492px;top:2058px;width:216px">VIEW ALL SERVICES <svg width="14" height="14" viewBox="0 0 14 14"><circle cx="7" cy="7" r="7" fill="#fff"/><path d="M5.5 4l3 3-3 3" stroke="#1fa06a" stroke-width="1.6" fill="none"/></svg></div>

<div class="badge" style="left:48px;top:2234px">03</div>
<h2 class="section-title" style="top:2268px">LATEST NEWS</h2>

<article class="news-card" style="left:99px">
  <div class="news-img" role="img" aria-label="Photo of two doctors reviewing a clipboard" style="background:linear-gradient(135deg,#9fb2be,#e7ecef 50%,#4c6476)"></div>
  <div class="news-body">
    <div class="news-title">IPSAM VOLUPTATEM</div>
    <div class="news-date">▦ APRIL 02,2018</div>
    <p class="news-text">At vero eos et accusam muset iusto odio dignissimos ducimus qui praesenm tm voluptatum deleniti atque</p>
    <div class="news-foot"><b>READ MORE ➜</b><span>35 comments</span></div>
  </div>
</article>
<article class="news-card" style="left:618px">
  <div class="news-img" role="img" aria-label="Photo of a woman having her hair washed at a salon" style="background:linear-gradient(135deg,#6b4a3a,#c9a98f 50%,#efe6dc)"></div>
  <div class="news-body">
    <div class="news-title">ACCUSAMUS ET IUSTO</div>
    <div class="news-date">▦ APRIL 08,2018</div>
    <p class="news-text">At vero eos et accusam muset iusto odio dignissimos ducimus qui praesenm tm voluptatum deleniti atque</p>
    <div class="news-foot"><b>READ MORE ➜</b><span>35 comments</span></div>
  </div>
</article>

<div class="rule"></div>
<h2 class="section-title" style="top:2743px">WHAT OUR CLIENTS SAY</h2>
<div class="badge" style="left:1046px;top:2731px">04</div>

<div class="side-arrow" style="left:25px"><svg width="12" height="12" viewBox="0 0 12 12"><path d="M8 1L3 6l5 5" stroke="#555" stroke-width="1.8" fill="none"/></svg></div>
<div class="side-arrow" style="left:1128px"><svg width="12" height="12" viewBox="0 0 12 12"><path d="M4 1l5 5-5 5" stroke="#555" stroke-width="1.8" fill="none"/></svg></div>

<article class="quote-card" style="left:99px">
  <div class="avatar" role="img" aria-label="Client portrait" style="background:linear-gradient(160deg,#8a5a48,#d7b39c)"></div>
  <div class="quote-mark">“</div>
  <div class="stars">★★★★★</div>
  <p class="quote">" At vero eos et accusamus et iustodio dignis simos ducimus qui blanditiipraesent iuvoluptatum ducimus deleniti atque quos "</p>
  <div class="who"><b>ELSA MARLOW,</b> Creative Manager</div>
</article>
<article class="quote-card" style="left:448px">
  <div class="avatar" role="img" aria-label="Client portrait" style="background:linear-gradient(160deg,#3d3d45,#b99b87)"></div>
  <div class="quote-mark">“</div>
  <div class="stars">★★★★★</div>
  <p class="quote">" At vero eos et accusamus et iustodio dignis simos ducimus qui blanditiipraesent iuvoluptatum ducimus deleniti atque quos "</p>
  <div class="who"><b>DARIO VENN,</b> Creative Manager</div>
</article>
<article class="quote-card" style="left:797px">
  <div class="avatar" role="img" aria-label="Client portrait" style="background:linear-gradient(160deg,#4a3428,#caa48a)"></div>
  <div class="quote-mark">“</div>
  <div class="stars">★★★★★</div>
  <p class="quote">" At vero eos et accusamus et iustodio dignis simos ducimus qui blanditiipraesent iuvoluptatum ducimus deleniti atque quos "</p>
  <div class="who"><b>NADIA CRELL,</b> Creative Manager</div>
</article>

<svg class="footer-curve" viewBox="0 0 1200 100" preserveAspectRatio="none">
  <path d="M0 90 Q600 -20 1200 90 L1200 100 L0 100Z" fill="#101d63"/>
  <path d="M0 78 Q600 -34 1200 78" stroke="#1fa06a" stroke-width="6" fill="none"/>
</svg>
<footer class="footer">
  <div class="f-head" style="left:99px">QUICK LINKS</div>
  <div class="f-head" style="left:296px">CONTACT DETAILS</div>
  <div class="f-head" style="left:671px">INQUIRE FORM</div>
  <ul class="f-links"><li>Home</li><li>About Us</li><li>Our Services</li><li>Testimonials</li><li>In The News</li><li>Contact Us</li></ul>
  <div class="f-contact">
    <div class="f-row"><svg width="18" height="18" viewBox="0 0 24 24"><path fill="#cfd4e8" d="M12 2a7 7 0 0 1 7 7c0 5-7 13-7 13S5 14 5 9a7 7 0 0 1 7-7zm0 4a3 3 0 1 0 0 6 3 3 0 0 0 0-6z"/></svg><span>123A, Sample Street, Sample<br>City, New State.</span></div>
    <div class="f-row"><svg width="18" height="18" viewBox="0 0 24 24"><path fill="#cfd4e8" d="M6.6 10.8a15 15 0 0 0 6.6 6.6l2.2-2.2c.3-.3.7-.4 1-.2 1.1.4 2.3.6 3.6.6.6 0 1 .4 1 1V20c0 .6-.4 1-1 1A17 17 0 0 1 3 4c0-.6.4-1 1-1h3.5c.6 0 1 .4 1 1 0 1.3.2 2.5.6 3.6.1.3 0 .7-.2 1z"/></svg><span>(+1) 123 4567 890</span></div>
    <div class="f-row"><svg width="18" height="18" viewBox="0 0 24 24"><path fill="#cfd4e8" d="M2 5h20v14H2zM4 7v.5l8 5 8-5V7z"/></svg><span>info@torvanerestorative.example</span></div>
  </div>
  <p class="f-note">Remember Torvane Center for all of your health improvement therapy, we are here to help you 24 hours a day!...</p>
  <div class="field" style="left:671px;top:132px;width:209px">Name</div>
  <div class="field" style="left:892px;top:132px;width:208px">Email</div>
  <div class="field" style="left:671px;top:188px;width:209px">Phone No</div>
  <div class="submit">SUBMIT</div>
  <div class="f-rule"></div>
  <div class="copy">Copyrights © 2018 Torvane Center Restorative Medicine. &nbsp;All Rights Reserved &nbsp; | &nbsp; Privacy Policy.</div>
  <div class="follow">FOLLOW US</div>
  <div class="socials"><span></span><span></span><span></span><span></span></div>
</footer>

</body>
</html>
```